Pinecrest Artisan League Membership

UPDATED files - 06/03/2021
Digital brochure needed for construction contractor related nonprofit organization.
Document will be primarily for digital viewing with potential for print version. Should be branded with our branding (logo attached). This is intended to be a multiple page document, plan to print and web (email) use. Standard Letter size document 8.5 x 11 inch
Portrait format preferred
The attached project brief includes a cover, 4 internal pages, and a back cover. This is flexible pending design layout
Target Market(s)
Residential construction business owners
Requirements
Must have
- See attached brief.Orange color palette: RGB: (253,153,0)
Nice to have
- See attached bief
Should not have
- No suit or ties. button up shirt okay, but not white collar worker.

```html
<!DOCTYPE html>
<html lang="en">
<head>
<meta charset="utf-8">
<title>Pinecrest Artisan League – Membership Brochure</title>
<link href="https://fonts.googleapis.com/css2?family=Outfit:wght@200;300;400;500;600;700;800&display=swap" rel="stylesheet">
<style>
:root{
  --orange:#fd9900;
  --orange-light:#fbbf5a;
  --charcoal:#333335;
  --ink:#2b2b2b;
  --body:#555;
  --rule:#f5b449;
  --backdrop:#ececec;
  --paper:#ffffff;
}
*{box-sizing:border-box;margin:0;padding:0}
html,body{width:1200px;height:3450px;overflow:hidden;background:var(--backdrop);font-family:"Outfit",sans-serif;color:var(--ink)}
.page{position:absolute;left:371px;width:458px;height:595px;background:var(--paper);overflow:hidden}
.abs{position:absolute}
.photo{position:absolute}
.brand{font-family:"Outfit",sans-serif;font-weight:800;color:var(--ink);display:flex;align-items:center;gap:6px;letter-spacing:.2px;line-height:1}
.brand .mark{width:9px;height:9px;background:var(--orange);flex:none}
.contact{font-size:6.5px;font-weight:600;line-height:17px;color:var(--ink)}
.h2{font-size:12px;font-weight:600;color:var(--ink)}
.h2 .light{font-weight:300}
.rule{height:1px;background:var(--rule)}
.p{font-size:6px;line-height:9px;color:var(--body)}
.footer{position:absolute;left:47px;right:46px;bottom:6px;height:14px;font-size:5.5px;font-weight:600;color:var(--ink)}
.footer .line{position:absolute;left:100px;right:140px;top:4px;height:1px;background:var(--rule)}
.footer .bar{position:absolute;left:0;bottom:0;width:100px;height:2px;background:var(--orange)}
.footer .right{position:absolute;right:0;top:0}
.ticks li{list-style:none;position:relative;padding-left:14px;font-size:6.5px;line-height:9px;font-weight:500;color:var(--body);margin-bottom:10px}
.ticks li svg{position:absolute;left:0;top:1px}
</style>
</head>
<body>

<!-- Cover -->
<section class="page" style="top:60px">
  <div class="photo" role="img" aria-label="Construction workers in hard hats and safety vests reviewing a laptop on site" style="left:0;top:0;width:458px;height:331px;background:linear-gradient(160deg,#cdbda4 0%,#8f8573 35%,#b7c24a 65%,#5c5a52 100%)"></div>
  <div class="abs" style="left:0;top:331px;width:386px;height:147px;background:var(--orange)"></div>
  <div class="abs" style="left:386px;top:331px;width:72px;height:69px;background:var(--charcoal)"></div>
  <div class="abs" style="left:347px;top:438px;width:39px;height:40px;background:var(--orange-light)"></div>
  <div class="abs" style="left:40px;top:355px;width:1.5px;height:100px;background:#fff"></div>
  <h1 class="abs" style="left:48px;top:354px;font-size:24px;line-height:24px;font-weight:200;color:#fff;letter-spacing:.3px">HELPING YOU REDUCE<br>RISKS AND INJURIES<br>WHILE IMPROVING<br>PROFITABILITY</h1>
  <div class="abs" style="left:39px;top:523px;width:2px;height:48px;background:var(--orange)"></div>
  <div class="abs contact" style="left:48px;top:521px">pinecrestartisans.org<br>hello@pinecrestartisans.org<br>555-014-2290</div>
  <div class="abs brand" style="right:40px;top:538px;font-size:14px"><span class="mark"></span>Pinecrest Artisan League</div>
</section>

<!-- Mission / About -->
<section class="page" style="top:745px">
  <div class="abs" style="left:47px;top:43px;width:190px">
    <div class="h2">Mission</div><div class="rule" style="margin:5px 0 10px"></div>
    <p class="p">To promote, educate and advance a diverse contractor community by providing pathways of accessibility to help build a stronger foundation for a better future.</p>
    <div class="h2" style="margin-top:28px">Vision</div><div class="rule" style="margin:5px 0 10px"></div>
    <p class="p">To become the preferred organization for construction contractors striving to be the best in their trade through education, training, and ongoing development.</p>
    <div class="h2" style="margin-top:28px">Diversity, Equity &amp; Inclusion</div><div class="rule" style="margin:5px 0 10px"></div>
    <p class="p">The League promotes and encourages open dialogue and positive working environments for BIPOC and other identity groups, to thrive within a contractor community and facilitate a more inclusive and resilient future.</p>
  </div>
  <div class="abs" style="left:277px;top:43px;width:134px">
    <div class="h2">About Us</div><div class="rule" style="margin:5px 0 10px"></div>
    <p class="p">The League is organized as a 501c6 membership organization supported by a 501c3 charitable foundation. Our foundation allows us to provide access to training and education resources to an underserved community of contractors, supporting them in developing a sustainable and profitable business.</p>
    <p class="p" style="margin-top:5px">We invite you to join a community of contractors who are better prepared to overcome challenges within the industry, empowering them to share ideas, lessons learned, proven practices, and insights with other industry leaders.</p>
    <div class="brand" style="margin-top:22px;font-size:12px;line-height:13px;align-items:flex-start"><span class="mark" style="margin-top:2px"></span>Pinecrest Artisan League</div>
  </div>
  <div class="photo" role="img" aria-label="Older contractor writing in a notebook at a desk" style="left:200px;top:300px;width:258px;height:295px;background:radial-gradient(ellipse at 70% 45%,#a39a88 0%,#cfc9bf 40%,rgba(255,255,255,0) 75%)"></div>
  <div class="abs" style="left:47px;top:331px;width:130px;height:19px;border-radius:10px;background:var(--orange);color:#fff;font-size:10px;font-weight:700;text-align:center;line-height:19px;letter-spacing:.3px">CORE VALUES</div>
  <ul class="abs ticks" style="left:59px;top:370px;width:110px">
    <li><svg width="9" height="9" viewBox="0 0 9 9"><rect x=".5" y=".5" width="8" height="8" fill="none" stroke="#fd9900"/><path d="M2 4.5l2 2 4-5" fill="none" stroke="#fd9900" stroke-width="1.2"/></svg>Empower through learning &amp; development</li>
    <li><svg width="9" height="9" viewBox="0 0 9 9"><rect x=".5" y=".5" width="8" height="8" fill="none" stroke="#fd9900"/><path d="M2 4.5l2 2 4-5" fill="none" stroke="#fd9900" stroke-width="1.2"/></svg>Strengthen &amp; sustain the industry</li>
    <li><svg width="9" height="9" viewBox="0 0 9 9"><rect x=".5" y=".5" width="8" height="8" fill="none" stroke="#fd9900"/><path d="M2 4.5l2 2 4-5" fill="none" stroke="#fd9900" stroke-width="1.2"/></svg>Build partnerships to benefit underserved communities</li>
    <li><svg width="9" height="9" viewBox="0 0 9 9"><rect x=".5" y=".5" width="8" height="8" fill="none" stroke="#fd9900"/><path d="M2 4.5l2 2 4-5" fill="none" stroke="#fd9900" stroke-width="1.2"/></svg>Act with integrity, respect, and honesty</li>
    <li><svg width="9" height="9" viewBox="0 0 9 9"><rect x=".5" y=".5" width="8" height="8" fill="none" stroke="#fd9900"/><path d="M2 4.5l2 2 4-5" fill="none" stroke="#fd9900" stroke-width="1.2"/></svg>Promote diversity, equity, and inclusion throughout the industry</li>
  </ul>
  <div class="footer"><span>pinecrestartisans.org</span><div class="line"></div><div class="bar"></div><span class="right">hello@pinecrestartisans.org &nbsp; 555-014-2290</span></div>
</section>

<!-- Technical assistance -->
<section class="page" style="top:1428px">
  <div class="abs" style="left:0;top:24px;width:458px;height:162px;background:linear-gradient(90deg,#2f2f31 0%,#3a3a3c 55%,#56575a 100%)"></div>
  <div class="abs" style="left:0;top:24px;width:458px;height:2px;background:var(--orange)"></div>
  <div class="abs" style="left:47px;top:44px;width:364px">
    <div class="h2" style="color:#fff">Technical <span class="light">Assistance</span></div>
    <div style="height:1px;background:rgba(255,255,255,.35);margin:6px 0 11px"></div>
    <p class="p" style="color:#e2e2e2">One of our primary goals is to provide technical assistance to the contractor community based on individual level of competency. We understand that the needs of contractors vary greatly based on experience, training, past mentorship.</p>
    <p class="p" style="color:#e2e2e2;margin-top:5px">Technical assistance takes many forms including business formation assistance, contractor licensing (OR, WA), insurance consulting, access to legal resources as well as assistance with government program funding (PPP Loans, business grants, scholarships), and various networking opportunities.</p>
    <p class="p" style="color:#e2e2e2;margin-top:5px">We also provide technical assistance in one-on-one settings as well as business workshops and ongoing assistance. Additionally, we offer assistance with state small-business initial and renewal applications.</p>
  </div>
  <div class="abs" style="left:0;top:218px;width:411px;height:128px;background:#fff;box-shadow:0 6px 14px rgba(0,0,0,.12)"></div>
  <svg class="abs" style="left:0;top:218px" width="70" height="128" viewBox="0 0 70 128"><path d="M0 2H60L66 10M0 126H50L66 104" fill="none" stroke="#fd9900" stroke-width="1"/></svg>
  <div class="abs" style="left:72px;top:226px;font-size:10px;font-weight:300;color:var(--ink);display:flex;align-items:center;gap:4px"><span style="width:8px;height:8px;border-radius:50%;background:var(--orange)"></span>SiteLogbook</div>
  <div class="photo" role="img" aria-label="Desktop, laptop and phone screens showing the safety logging app" style="left:32px;top:248px;width:120px;height:80px;background:linear-gradient(135deg,#dfe7ef,#9fb4c7)"></div>
  <div class="abs" style="left:177px;top:227px;width:224px">
    <div class="h2">Safety &amp; Compliance – <span class="light">SiteLogbook</span></div>
    <div class="rule" style="margin:5px 0 10px"></div>
    <p class="p">SiteLogbook.app is a secure, web-based application that enables employers to create each state's first report of injury, track injuries, and view injury metrics in real-time. The software includes the ability to automatically generate and download PDF versions of OSHA forms 301, 300, and 300A to print, share, or email.</p>
    <p class="p" style="margin-top:5px">Works with all devices: computers, tablets, and smartphones. Once data is entered and intuitively updated on all other forms, SiteLogbook will automatically generate benchmark figures with no additional input by location and log.</p>
  </div>
  <div class="photo" role="img" aria-label="Contractor in orange hard hat and vest using a tablet beside a colleague" style="left:250px;top:362px;width:208px;height:233px;background:radial-gradient(ellipse at 55% 55%,#d2683a 0%,#b4a793 45%,rgba(255,255,255,0) 78%)"></div>
  <div class="abs" style="left:47px;top:376px;width:215px">
    <div style="font-size:13px;font-weight:700;color:var(--orange)">CrewSafe</div>
    <p class="p" style="margin-top:5px">Our partnership with CrewSafe gives you the tools you need to protect your workers, meet compliance requirements, and create a positive workspace environment for your employees and others you may work with. CrewSafe's staff of safety professionals, safety trainers, and administrative staff combined with innovative technology has helped thousands of contractors across the nation save money and improve efficiency.</p>
    <div style="font-size:5.5px;font-weight:700;color:var(--orange);letter-spacing:.8px;margin:9px 0 5px">INCLUDED IN THE MOBILE APP ARE THE FOLLOWING:</div>
    <ul class="ticks">
      <li style="margin-bottom:2px;font-size:5.5px;line-height:8px"><svg width="7" height="7" viewBox="0 0 9 9"><rect x=".5" y=".5" width="8" height="8" fill="none" stroke="#fd9900"/><path d="M2 4.5l2 2 4-5" fill="none" stroke="#fd9900" stroke-width="1.2"/></svg>Over 1,200 bilingual (Spanish/English) safety lessons with digital signoff rosters</li>
      <li style="margin-bottom:2px;font-size:5.5px;line-height:8px"><svg width="7" height="7" viewBox="0 0 9 9"><rect x=".5" y=".5" width="8" height="8" fill="none" stroke="#fd9900"/><path d="M2 4.5l2 2 4-5" fill="none" stroke="#fd9900" stroke-width="1.2"/></svg>An online form builder to create job and equipment-specific inspection forms</li>
      <li style="margin-bottom:2px;font-size:5.5px;line-height:8px"><svg width="7" height="7" viewBox="0 0 9 9"><rect x=".5" y=".5" width="8" height="8" fill="none" stroke="#fd9900"/><path d="M2 4.5l2 2 4-5" fill="none" stroke="#fd9900" stroke-width="1.2"/></svg>Mobile-accessible document storage repository</li>
      <li style="margin-bottom:2px;font-size:5.5px;line-height:8px"><svg width="7" height="7" viewBox="0 0 9 9"><rect x=".5" y=".5" width="8" height="8" fill="none" stroke="#fd9900"/><path d="M2 4.5l2 2 4-5" fill="none" stroke="#fd9900" stroke-width="1.2"/></svg>Live monthly webinars addressing safety topics</li>
    </ul>
  </div>
  <div class="footer"><span>pinecrestartisans.org</span><div class="line"></div><div class="bar"></div><span class="right" style="color:#fff">hello@pinecrestartisans.org &nbsp; 555-014-2290</span></div>
</section>

<!-- Education / Directory -->
<section class="page" style="top:2112px">
  <div class="abs" style="left:47px;top:43px;width:166px">
    <div class="h2">Contractor Education</div><div class="rule" style="margin:5px 0 9px"></div>
    <p class="p" style="font-weight:700;font-style:italic;color:var(--ink)">We provide education through live classes, training workshops, and via eLearning courses. We provide in-class training for EPA/RRP Certification, CPR/First Aid certification, Fall Protection certification, and the Oregon CCB 16-hour Pre-licensing training.</p>
    <p class="p" style="margin-top:10px">We also offer a full suite of online construction education courses to help contractors learn at their own pace and convenience. Courses are mobile-friendly and available in English or Spanish.</p>
    <p class="p" style="margin-top:4px">Our online course catalog includes:</p>
  </div>
  <div class="abs" style="left:224px;top:45px;width:1px;height:520px;background:#e6e6e6"></div>
  <svg class="abs" style="left:40px;top:235px" width="180" height="330" viewBox="0 0 180 330" font-family="Outfit, sans-serif" font-size="6" font-weight="600" fill="#2b2b2b">
    <line x1="90" y1="0" x2="90" y2="315" stroke="#fd9900" stroke-width="1.2"/>
    <g fill="#fff" stroke="#fd9900" stroke-width="1.5">
      <circle cx="90" cy="10" r="10"/><circle cx="90" cy="55" r="10"/><circle cx="90" cy="100" r="10"/><circle cx="90" cy="145" r="10"/><circle cx="90" cy="190" r="10"/><circle cx="90" cy="235" r="10"/><circle cx="90" cy="280" r="10"/>
    </g>
    <g stroke="#fd9900" stroke-width="1.2">
      <line x1="100" y1="10" x2="108" y2="10"/><line x1="72" y1="55" x2="80" y2="55"/><line x1="100" y1="100" x2="108" y2="100"/><line x1="72" y1="145" x2="80" y2="145"/><line x1="100" y1="190" x2="108" y2="190"/><line x1="72" y1="235" x2="80" y2="235"/><line x1="100" y1="280" x2="108" y2="280"/>
    </g>
    <g fill="none" stroke="#555" stroke-width=".8">
      <path d="M85 12a5 5 0 0 1 10 0zM84 12h12"/>
      <path d="M85 53h10l-2-2M95 57H85l2 2"/>
      <rect x="86" y="96" width="8" height="8"/>
      <rect x="85" y="142" width="10" height="7"/>
      <path d="M90 185l5 9h-10zM90 188v3"/>
      <circle cx="90" cy="233" r="3"/><path d="M86 240h8"/>
      <path d="M90 285v-6M90 281l-3-3M90 280l3-3"/>
    </g>
    <text x="112" y="9">OSHA 10 &amp; 30</text><text x="112" y="16">training</text>
    <text x="68" y="53" text-anchor="end">Trade-specific</text><text x="68" y="60" text-anchor="end">skills</text>
    <text x="112" y="98">Safety</text><text x="112" y="105">courses</text>
    <text x="68" y="143" text-anchor="end">Administrative</text><text x="68" y="150" text-anchor="end">courses</text>
    <text x="112" y="192">HAZWOPER</text>
    <text x="68" y="233" text-anchor="end">Construction</text><text x="68" y="240" text-anchor="end">management</text>
    <text x="112" y="278">Environmental</text><text x="112" y="285">exposure</text>
    <text x="90" y="303" text-anchor="middle">And much more…</text>
  </svg>
  <div class="abs brand" style="left:245px;top:45px;font-size:11px"><span class="mark"></span>Pinecrest Artisan League</div>
  <div class="abs" style="left:245px;top:80px;width:166px">
    <p class="p">We also offer targeted training tracks in specific skillsets to promote business development necessary to operate an efficient business.</p>
    <p class="p" style="font-style:italic;margin-top:3px">Skillsets include:</p>
    <ul style="margin-top:10px">
      <li style="list-style:none;display:flex;align-items:center;gap:10px;font-size:6.5px;color:var(--ink);height:26px"><svg width="16" height="14"><rect x="1" y="3" width="14" height="10" fill="none" stroke="#fd9900"/><path d="M5 3V1h6v2" fill="none" stroke="#fd9900"/></svg>Business operations</li>
      <li style="list-style:none;display:flex;align-items:center;gap:10px;font-size:6.5px;color:var(--ink);height:26px"><svg width="16" height="14"><path d="M8 1v12M2 4h12M2 4l-1 5h4zM14 4l-1 5h4" fill="none" stroke="#fd9900"/></svg>Business Law &amp; Contracts</li>
      <li style="list-style:none;display:flex;align-items:center;gap:10px;font-size:6.5px;color:var(--ink);height:26px"><svg width="16" height="14"><circle cx="8" cy="7" r="6" fill="none" stroke="#fd9900"/><path d="M8 3v8" stroke="#fd9900"/></svg>Understanding financials</li>
      <li style="list-style:none;display:flex;align-items:center;gap:10px;font-size:6.5px;color:var(--ink);height:26px"><svg width="16" height="14"><path d="M2 10a6 6 0 0 1 12 0zM1 10h14" fill="none" stroke="#fd9900"/></svg>Safety &amp; Compliance training</li>
      <li style="list-style:none;display:flex;align-items:center;gap:10px;font-size:6.5px;color:var(--ink);height:26px"><svg width="16" height="14"><circle cx="8" cy="7" r="2" fill="#fd9900"/><path d="M8 1v4M8 9v4M2 7h4M10 7h4" stroke="#fd9900"/></svg>Marketing &amp; Networking</li>
      <li style="list-style:none;display:flex;align-items:center;gap:10px;font-size:6.5px;color:var(--ink);height:26px"><svg width="16" height="14"><circle cx="8" cy="4" r="2.5" fill="none" stroke="#fd9900"/><path d="M3 13a5 5 0 0 1 10 0" fill="none" stroke="#fd9900"/></svg>Business Management / HR</li>
    </ul>
    <div class="h2" style="margin-top:10px">Directory for Contractors</div><div class="rule" style="margin:5px 0 10px"></div>
    <div style="display:flex;gap:6px"><span style="flex:none;width:14px;height:14px;border-radius:50%;background:var(--orange)"></span>
      <p class="p"><b style="color:var(--ink)">BuilderFinder.net</b> is a FREE effortless way for contractors to connect with property owners to search for a contractor in their local area. As marketing has evolved, contractors need to adapt a variety of online tools and technologies to help gain more online visibility which will result in more business for you.</p></div>
    <p class="p" style="margin-top:5px">The site gives instant access to residential and commercial contractors, an online bid request system, links to the contractor's social media pages and a review system all in one spot.</p>
    <p class="p" style="margin-top:5px">Create your business profile and easily manage your unlimited FREE Bid requests, reviews, social media, photo gallery, video links just to name a few. Having a profile listing adds legitimacy to your business.</p>
    <p class="p" style="margin-top:5px">A prime advantage of having your business listed is the SEO and relevant incoming "links to your business". Link building is an important building block of any SEO campaign.</p>
  </div>
  <div class="footer"><span>pinecrestartisans.org</span><div class="line"></div><div class="bar"></div><span class="right">hello@pinecrestartisans.org &nbsp; 555-014-2290</span></div>
</section>

<!-- Back cover -->
<section class="page" style="top:2796px">
  <div class="photo" role="img" aria-label="Silhouette of building scaffolding against a sunset sky" style="left:0;top:0;width:458px;height:475px;background:linear-gradient(180deg,#3f6f9c 0%,#8fa9b6 30%,#e0a53a 62%,#8a4a12 82%,#2a1608 100%)"></div>
  <div class="abs" style="left:40px;top:50px;width:1.5px;height:42px;background:var(--orange)"></div>
  <div class="abs contact" style="left:47px;top:48px;color:#fff;line-height:14px">Pinecrest Artisan League<br>2400 Alder Ridge Rd., Suite 210<br>Fairview, OR 97000</div>
  <div class="abs" style="left:40px;top:114px;width:1.5px;height:42px;background:var(--orange)"></div>
  <div class="abs contact" style="left:47px;top:112px;color:#fff;line-height:14px">Office: (555) 014-2290<br>Fax: 555.014.7731<br>support@pinecrestartisans.org</div>
  <div class="abs" style="left:0;top:475px;width:386px;height:30px;background:linear-gradient(90deg,var(--orange),#fbad2c)"></div>
  <div class="abs" style="left:386px;top:475px;width:26px;height:30px;background:var(--orange-light)"></div>
  <div class="abs" style="left:412px;top:475px;width:46px;height:30px;background:var(--charcoal)"></div>
  <div class="abs brand" style="left:47px;top:552px;font-size:12px"><span class="mark"></span>Pinecrest Artisan League</div>
  <div class="abs" style="right:46px;top:555px;font-size:6.5px;font-weight:600">pinecrestartisans.org</div>
</section>

</body>
</html>
```